environmentalist needs a bumper sticker design

The bumper sticker should say, "There is no Planet B."

thank you for the designs so far. Some have asked for more direction of my thinking. You've probably heard people talk of "Plan A" and "Plan B" when they want to consider alternatives. "There is no Planet B" reminds us that there are no alternatives. The question is, how best to encourage people to act? Research indicates that making people fearful is less effective (although certainly we have plenty to fear). It is more effective to stir emotions of caring and attachment. For example, designs that show the earth as a beautiful planet, or aspects of the earth (e.g., trees and mountains or whatever) remind us of what we love and want to care for.

```html
<!DOCTYPE html>
<html lang="en">
<head>
<meta charset="utf-8">
<title>There Is No Planet B — Bumper Sticker</title>
<link rel="stylesheet" href="https://fonts.googleapis.com/css2?family=Source+Sans+3:wght@700&display=swap">
<style>
  :root {
    --page: #ffffff;
    --shadow: #c9c9cf;
    --sky: #bdd3ea;
    --field: #76973f;
    --field-light: #86a651;
    --ink-dark: #231c1a;
    --ink-light: #ffffff;
    --letter-veil: rgba(238, 244, 232, 0.82);
  }
  html, body {
    margin: 0;
    padding: 0;
    width: 1200px;
    height: 1109px;
    overflow: hidden;
    background: var(--page);
  }
  .sticker {
    position: relative;
    width: 1200px;
    height: 1109px;
    font-family: "Source Sans 3", "Myriad Pro", Arial, sans-serif;
    font-weight: 700;
  }
  .sticker-art {
    position: absolute;
    left: 0;
    top: 0;
  }
  .headline {
    position: absolute;
    margin: 0;
    line-height: 1;
    white-space: nowrap;
    letter-spacing: 0;
  }
  .headline-top {
    color: var(--ink-dark);
    font-size: 128px;
    top: 165px;
    left: 278px;
    word-spacing: 100px;
  }
  .headline-middle {
    color: var(--ink-light);
    font-size: 134px;
    top: 292px;
    left: 218px;
    letter-spacing: -1px;
  }
  .headline-letter {
    color: var(--letter-veil);
    font-size: 600px;
    top: 378px;
    left: 434px;
  }
</style>
</head>
<body>
  <div class="sticker">
    <svg class="sticker-art" width="1200" height="1109" viewBox="0 0 1200 1109">
      <rect class="sticker-shadow" x="228" y="156" width="758" height="778" fill="var(--shadow)"/>
      <rect class="sticker-sky" x="206" y="134" width="772" height="784" fill="var(--sky)"/>
      <defs>
        <linearGradient id="field-tone" x1="0" y1="0" x2="0" y2="1">
          <stop offset="0" stop-color="var(--field-light)"/>
          <stop offset="1" stop-color="var(--field)"/>
        </linearGradient>
      </defs>
      <path class="sticker-field" role="img"
            aria-label="Grassy field dotted with cut tree stumps"
            d="M206 302 Q592 262 978 302 L978 918 L206 918 Z"
            fill="url(#field-tone)"/>
    </svg>
    <h1 class="headline headline-top">THERE IS</h1>
    <p class="headline headline-middle">NO PLANET</p>
    <p class="headline headline-letter">B</p>
  </div>
</body>
</html>
```